Thorne Legal PC business card. National Consumer Law Firm with principal office in San Francisco. We maintain additional offices in Meridian, Mississippi and Birmingham, Alabama. We protect consumers against unscrupulous mega corporations. We want to covey integrity and a willingness to take on the Goliaths of the corporate world. I like red accents. Try to use uploaded picture of Harbor Arch Span or a sketch. Licensed in California, Alabama and Mississippi. Main office: 318 Alder Ave. #407, San Francisco, CA 94110, ph. 415/555-0182, 800/555-0147 (fax), 205/555-0136 (AL).
www.thornelegalpc.example
www.claimwatch.example.
At top--Public Claim Advocacy in red. Also Thorne Legal PC at top in red. Then red horizontal line please. Or if you have another idea. I have not seen new logo.
After line on left at top
H. Dwight Thorne
Attorney
Cell 205/555-0194
dwight@thornelegalpc.example
Offices: San Francisco, CA, Birmingham, AL, Charlotte, NC and Meridian, MS

I asked that the very bottom of the BUSINESS CARD TO SAY "Offices in California, North Carolina, Alabama and Mississippi NOT STATES WHERE I AM LICENSED. I.E., I AM NOT LICENSED IN NOTH CAROLINA I NEED NEW FILES IF YOU CAN GET THEM IN THE MORNING MY TIME. WHERE CAN I FIND THE NEW FILES ONCE YOU MODIFY.

for North Carolina, I need an asterick where it is listed. "not licensed will associate counsel" AGAIN NORTH CAROLINA IS 2 WORDS WITH A SPACE BETWEEN THEM

For Biz card, put tollfree number (888)555-0129 and toll free fax (800)555-0147 somewhere like below my cell number or wherever you can. States where I have offices at the bottom: California, North Carolina, Alabama and Mississippi.

For Biz card, put tollfree number (888)555-0129 and toll free fax (800)555-0147 somewhere like below my cell number or wherever you can. States where I have offices at the bottom: California, North Carolina, Alabama and Mississippi. AstericK *North Carolina--not licensed will associate co-counel. Same with letterhead and website. I need to disclose not licensed to practice in North Carolina.

```html
<!DOCTYPE html>
<html lang="en">
<head>
<meta charset="utf-8">
<title>Thorne Legal PC – Business Card</title>
<link rel="stylesheet" href="https://fonts.googleapis.com/css2?family=Oxygen:wght@300;400;700&display=swap">
<style>
  :root {
    --canvas: #f1f0ec;
    --photo-light: #8a8572;
    --photo-mid: #6a6655;
    --photo-dark: #3d3a2f;
    --band-grey: rgba(128, 122, 100, 0.55);
    --band-red: rgba(236, 68, 46, 0.93);
    --stripe-red: rgba(214, 40, 34, 0.95);
    --accent-red: #e0342a;
    --ink-light: #ffffff;
    --ink-soft: #f1efe8;
  }
  html, body {
    margin: 0;
    width: 1200px;
    height: 1000px;
    overflow: hidden;
    background: var(--canvas);
    font-family: "Oxygen", "Helvetica Neue", Arial, sans-serif;
  }
  .business-card {
    position: absolute;
    left: 127px;
    top: 233px;
    width: 945px;
    height: 534px;
    overflow: hidden;
    color: var(--ink-light);
    box-shadow: 0 2px 6px rgba(0,0,0,0.18);
  }
  .card-photo {
    position: absolute;
    inset: 0;
    background:
      radial-gradient(ellipse at 30% 55%, rgba(255,255,255,0.08), transparent 60%),
      linear-gradient(180deg, var(--photo-light) 0%, var(--photo-mid) 55%, var(--photo-dark) 100%);
  }
  .tagline-band {
    position: absolute;
    left: 0; top: 0;
    width: 100%; height: 81px;
    background: var(--band-grey);
    display: flex; align-items: center; justify-content: center;
  }
  .tagline {
    margin: 0;
    font-size: 37px;
    font-weight: 700;
    letter-spacing: 3px;
    text-transform: uppercase;
  }
  .brand-band {
    position: absolute;
    left: 0; top: 81px;
    width: 100%; height: 130px;
    background: var(--band-red);
    display: flex; align-items: center; justify-content: center;
  }
  .brand-name {
    font-size: 62px;
    font-weight: 300;
    letter-spacing: 1px;
    text-transform: uppercase;
    color: var(--ink-light);
  }
  .attorney-block {
    position: absolute;
    left: 94px; top: 228px;
    font-size: 19px;
    line-height: 28px;
  }
  .attorney-name {
    font-size: 25px;
    font-weight: 700;
    letter-spacing: 0.5px;
    margin: 0;
    line-height: 32px;
  }
  .attorney-title {
    color: var(--accent-red);
    font-size: 18px;
    line-height: 20px;
    margin: 0 0 12px;
  }
  .contact-line { margin: 0; color: var(--ink-soft); }
  .label { color: var(--accent-red); }
  .office-block {
    position: absolute;
    right: 97px; top: 232px;
    text-align: right;
    font-size: 20px;
    line-height: 31px;
    color: var(--ink-soft);
    font-style: normal;
  }
  .office-block p { margin: 0; }
  .web-band {
    position: absolute;
    left: 0; top: 417px;
    width: 100%; height: 34px;
    background: var(--stripe-red);
    display: flex; align-items: center; justify-content: center;
    font-size: 21px;
    letter-spacing: 2px;
  }
  .web-band .divider { margin: 0 16px; }
  .office-states {
    position: absolute;
    left: 0; top: 462px;
    width: 100%;
    text-align: center;
    margin: 0;
    font-size: 17px;
    line-height: 24px;
    font-weight: 700;
    letter-spacing: 2px;
    text-transform: uppercase;
  }
  .office-states .mark { color: var(--accent-red); }
  .disclaimer {
    position: absolute;
    left: 0; top: 494px;
    width: 100%;
    text-align: center;
    margin: 0;
    font-size: 14px;
    line-height: 20px;
    letter-spacing: 0.5px;
    color: var(--ink-soft);
  }
  .disclaimer .mark { color: var(--accent-red); }
</style>
</head>
<body>
  <section class="business-card">
    <div class="card-photo" role="img" aria-label="Sepia photograph of the Harbor Arch Span suspension bridge over the bay"></div>

    <header class="tagline-band">
      <h1 class="tagline">Public Claim Advocacy</h1>
    </header>

    <div class="brand-band">
      <span class="brand-name">Thorne Legal PC</span>
    </div>

    <div class="attorney-block">
      <p class="attorney-name">H. Dwight Thorne</p>
      <p class="attorney-title">Attorney</p>
      <p class="contact-line">205/555-0194 <span class="label">(cell)</span></p>
      <p class="contact-line">(888)555-0129 <span class="label">(toll free)</span></p>
      <p class="contact-line">(800)555-0147 <span class="label">(toll free fax)</span></p>
      <p class="contact-line">dwight@thornelegalpc.example</p>
    </div>

    <address class="office-block">
      <p>318 Alder Ave. #407</p>
      <p>San Francisco, CA 94110</p>
      <p>415/555-0182 <span class="label">(CA)</span></p>
      <p>800/555-0147 <span class="label">(fax)</span></p>
      <p>205/555-0136 <span class="label">(AL)</span></p>
    </address>

    <div class="web-band">
      <span>www.thornelegalpc.example</span><span class="divider">|</span><span>www.claimwatch.example</span>
    </div>

    <p class="office-states">Offices in California, North Carolina<span class="mark">*</span>, Alabama and Mississippi</p>
    <p class="disclaimer"><span class="mark">*</span>North Carolina – not licensed, will associate co-counsel</p>
  </section>
</body>
</html>
```